TARO PTY LTD - Business Cards

Design a modern business card - using the attached Designs.
Same design as on the front, apart from the names/numbers/emails to be different.
We want the cards to be very glossy to stand out, do I think the simple black/white/metallic will be effective.
Both lots of details below:

Lyle Marrick
Director
lyle_taro@quintmail.example
0493 628 304

Simon Prowle
Director
simon_taro@quintmail.example
0438 514 209

```html
<!DOCTYPE html>
<html lang="en">
<head>
<meta charset="utf-8">
<title>TARO PTY LTD – Business Cards</title>
<link rel="stylesheet" href="https://fonts.googleapis.com/css2?family=Open+Sans:wght@400;700&display=swap">
<style>
  :root {
    --backdrop: #e9e8e6;
    --card-white: #ffffff;
    --card-silver: #e4e5e7;
    --ink-dark: #2b2c2e;
    --band-top: #4a4b4e;
    --band-bottom: #0d0d0e;
    --text-light: #f4f4f4;
    --text-muted: #c9c9c9;
    --shadow: rgba(0, 0, 0, 0.22);
  }
  * { margin: 0; padding: 0; box-sizing: border-box; }
  html, body {
    width: 1200px; height: 913px; overflow: hidden;
    background: var(--backdrop);
    font-family: "Open Sans", Arial, sans-serif;
  }
  .canvas { position: relative; width: 1200px; height: 913px; }

  .card {
    position: absolute; width: 500px; height: 300px;
    border-radius: 4px; overflow: hidden;
    box-shadow: 0 14px 30px var(--shadow), 0 2px 4px var(--shadow);
  }
  .card--front { left: 80px; top: 150px; }
  .card--back  { left: 620px; top: 460px; }

  .card__surface {
    position: absolute; inset: 0;
    background: linear-gradient(135deg, var(--card-white) 0%, var(--card-silver) 55%, var(--card-white) 100%);
  }

  .brand {
    position: absolute; display: flex; align-items: center; gap: 12px;
    color: var(--ink-dark); font-weight: 700; letter-spacing: 1px; white-space: nowrap;
  }
  .brand__dot { border-radius: 50%; background: var(--ink-dark); }
  .card--front .brand { left: 50%; top: 50%; transform: translate(-50%, -50%); font-size: 34px; }
  .card--front .brand__dot { width: 30px; height: 30px; }
  .card--back .brand { left: 50%; top: 52px; transform: translate(-50%, -50%); font-size: 22px; }
  .card--back .brand__dot { width: 20px; height: 20px; }

  .card__band { position: absolute; inset: 0; }

  .contact { position: absolute; color: var(--text-light); white-space: nowrap; }
  .contact--left  { left: 26px; top: 190px; }
  .contact--right { left: 262px; top: 130px; }
  .contact__name { font-size: 17px; font-weight: 700; line-height: 1.15; }
  .contact__role { font-size: 10px; color: var(--text-muted); margin-bottom: 6px; }
  .contact__line { display: flex; align-items: center; gap: 8px; font-size: 12px; line-height: 1.6; }
  .contact__icon { width: 12px; height: 12px; flex: none; }
</style>
</head>
<body>
<main class="canvas">

  <section class="card card--front" aria-label="Card front">
    <div class="card__surface"></div>
    <div class="brand"><span class="brand__dot"></span>TARO PTY LTD</div>
  </section>

  <section class="card card--back" aria-label="Card back">
    <div class="card__surface"></div>
    <svg class="card__band" viewBox="0 0 500 300" width="500" height="300" aria-hidden="true">
      <defs>
        <linearGradient id="bandShade" x1="0" y1="0" x2="0" y2="1">
          <stop offset="0" stop-color="#4a4b4e"/>
          <stop offset="1" stop-color="#0d0d0e"/>
        </linearGradient>
      </defs>
      <polygon points="0,160 500,82 500,300 0,300" fill="url(#bandShade)"/>
    </svg>

    <div class="brand"><span class="brand__dot"></span>TARO PTY LTD</div>

    <div class="contact contact--right">
      <div class="contact__name">Simon Prowle</div>
      <div class="contact__role">Director</div>
      <div class="contact__line">
        <svg class="contact__icon" viewBox="0 0 12 12" aria-hidden="true"><path d="M1 4 Q6 0 11 4 L9.5 5.5 L8 4.5 L4 4.5 L2.5 5.5 Z M3 6 H9 L10 11 H2 Z" fill="#f4f4f4"/></svg>
        <span>0438 514 209</span>
      </div>
      <div class="contact__line">
        <svg class="contact__icon" viewBox="0 0 12 12" aria-hidden="true"><rect x="0.5" y="2.5" width="11" height="7" fill="none" stroke="#f4f4f4"/><path d="M0.5 2.5 L6 7 L11.5 2.5" fill="none" stroke="#f4f4f4"/></svg>
        <span>simon_taro@quintmail.example</span>
      </div>
    </div>

    <div class="contact contact--left">
      <div class="contact__name">Lyle Marrick</div>
      <div class="contact__role">Director</div>
      <div class="contact__line">
        <svg class="contact__icon" viewBox="0 0 12 12" aria-hidden="true"><path d="M1 4 Q6 0 11 4 L9.5 5.5 L8 4.5 L4 4.5 L2.5 5.5 Z M3 6 H9 L10 11 H2 Z" fill="#f4f4f4"/></svg>
        <span>0493 628 304</span>
      </div>
      <div class="contact__line">
        <svg class="contact__icon" viewBox="0 0 12 12" aria-hidden="true"><rect x="0.5" y="2.5" width="11" height="7" fill="none" stroke="#f4f4f4"/><path d="M0.5 2.5 L6 7 L11.5 2.5" fill="none" stroke="#f4f4f4"/></svg>
        <span>lyle_taro@quintmail.example</span>
      </div>
    </div>
  </section>

</main>
</body>
</html>
```